High-End Medical Center Website Design Project

This design is part of a well thought-out project by an experienced project manager / developer. The approved wireframe is attached. Creative interpretations / suggestions based on the layout encouraged.

The design is for a new state-of-the-art medical center located in Dallas, Texas. The target audience would likely be individuals (approx. 60% female /40% male) who are the healthcare decision-makers for their families. They would likely have insurance and be inclined to seek out top-quality care.

Potential clients would choose this client over others in their industry because the medical center is physician owned, meaning it is patient-focused rather than profit-focused. The facility is brand new, featuring the latest technology. (This includes an amazing waiting room featuring WiFi and docking stations.) The physicians are hand-picked by referral only.

The look of the site should be extremely clean. We are going for a well-organized, professional look with a bit of a warm glow (interpret that however you like). Use crisp corners and the colors in the logo.

Think modern, clean with some great use of color / font.

We can get lovely photography of the medical center once construction is complete. Feel free to use an "example image" behind the Featured Area ("Physician Owned. Patient-Focused") if you like. We are open to ideas.

ONE CHANGE REQUESTED IN THE WIREFRAME:

Remove the "Connect" 1/4 page footer area and replace with a quick contact form. You may swap the "Locations" area with the form if desired. Put social media icons at the top left of the page in the top header area.

(Note: Please use social media icons that match the design rather than standard icons. We preferred not placing the icons at the top, but the client requested this. Let's not bring more attention to them than necessary.)
Updates

We're custom programming this site, so there's no need to base it on a template. Also, we would prefer not to use typical "seen everywhere" stock images.Thanks.

Industry/Entity Type

Construction

Requirements
Must have
• Follow the wireframe. This has been approved.
Nice to have
• Examples of what hover states, links or dropdowns might look like.

```html
<!DOCTYPE html>
<html lang="en">
<head>
<meta charset="utf-8">
<title>Northvale Medical Center</title>
<link href="https://fonts.googleapis.com/css2?family=PT+Sans:wght@400;700&family=Open+Sans:wght@400;600&display=swap" rel="stylesheet">
<style>
:root{
  --blue:#0c4da2;
  --blue-dark:#0a3f86;
  --sky:#29a8e0;
  --teal:#2a9aa8;
  --ink:#2b2b2b;
  --muted:#777;
  --line:#d8d8d8;
  --footer:#3b3b3b;
  --footer-dark:#2a2a2a;
}
*{margin:0;padding:0;box-sizing:border-box}
html,body{width:784px;height:1200px;overflow:hidden;background:#fff}
body{position:relative;font-family:'Open Sans',sans-serif;color:var(--ink)}
.abs{position:absolute}
.topbar{left:0;top:0;width:784px;height:16px;background:var(--blue);color:#fff;font-size:8px;display:flex;justify-content:flex-end;align-items:center;gap:14px;padding-right:100px}
.topbar span{display:flex;align-items:center;gap:4px}
.header{left:0;top:16px;width:784px;height:84px;background:linear-gradient(#f4f4f4,#fff 40%)}
.logo{left:87px;top:47px;display:flex;align-items:center;gap:6px;font-family:'PT Sans',sans-serif;font-weight:700;font-size:15px;color:var(--blue);letter-spacing:.4px}
.logo i{width:11px;height:11px;background:var(--blue);display:block}
.nav{left:406px;top:52px;display:flex;gap:15px;font-size:8.5px;color:var(--ink)}
.hero{left:0;top:100px;width:784px;height:302px;background:linear-gradient(100deg,#2c3038 0%,#5b616a 40%,#8a8f92 60%,#3f434a 100%)}
.hero h1{position:absolute;left:0;width:784px;top:123px;text-align:center;font-family:'PT Sans',sans-serif;font-weight:400;font-size:44px;color:#fff;text-shadow:0 2px 6px rgba(0,0,0,.5)}
.feature{position:absolute;width:176px;text-align:center}
.feature h3{font-family:'PT Sans',sans-serif;font-weight:400;font-size:12px}
.feature p{font-family:Arial,sans-serif;font-size:8.5px;line-height:15px;color:#444;margin:13px 22px 0}
.btn{display:inline-block;margin-top:17px;background:var(--sky);color:#fff;font-family:Arial,sans-serif;font-size:8.5px;padding:3px 4px;border-radius:2px;box-shadow:0 0 0 1px #bfe4f5}
.cards{left:85px;top:614px;width:625px;height:215px;border-bottom:1px solid var(--line)}
.card{position:absolute;top:7px;width:190px}
.card .pic{width:190px;height:99px}
.card h4{font-family:'PT Sans',sans-serif;font-weight:700;font-size:11px;margin:8px 0 0 2px;letter-spacing:.2px}
.card .rule{margin:12px 0 0 2px;height:4px;border-top:1px dotted var(--line);position:relative;width:164px}
.card .rule:before{content:"";position:absolute;left:0;top:-3px;width:4px;height:4px;border-radius:50%;background:var(--sky)}
.card p{font-size:7.4px;line-height:12px;color:var(--muted);margin:12px 0 0 2px}
.welcome-pic{left:84px;top:874px;width:101px;height:97px;background:linear-gradient(120deg,#d9dde2,#9bb0c6 60%,#e8e3dc)}
.welcome{left:196px;top:872px;width:240px}
.welcome h2{font-family:'PT Sans',sans-serif;font-weight:400;font-size:17px}
.welcome p{font-size:8.2px;line-height:12.5px;color:#444;margin-top:9px}
.testi{left:531px;top:873px;width:180px}
.testi h2{font-family:'PT Sans',sans-serif;font-weight:400;font-size:15px}
.bubble{margin-top:6px;background:var(--teal);color:#fff;font-size:7.4px;line-height:11.8px;padding:6px 8px;height:61px;position:relative}
.bubble:after{content:"";position:absolute;right:26px;bottom:-16px;border-left:18px solid transparent;border-top:16px solid var(--teal)}
.author{text-align:right;margin-top:9px;padding-right:52px;font-size:7px;color:#555;line-height:9px;position:relative}
.author b{font-family:'PT Sans',sans-serif;color:var(--ink)}
.avatar{position:absolute;right:25px;top:-3px;width:21px;height:24px;background:#d6d6d6;border:1px solid #bbb}
.pager{right:73px;top:995px;display:flex;gap:2px;align-items:center;font-size:5.5px;color:#666;border:1px solid #ddd;border-radius:6px;padding:1px 3px}
.pager i{width:5px;height:5px;border-radius:50%;background:#bbb;display:block}
.pager i.on{background:#555}
.footer{left:0;top:1010px;width:784px;height:152px;background:var(--footer);color:#cfcfcf}
.fcol{position:absolute;top:20px}
.fcol h5{font-family:'PT Sans',sans-serif;font-weight:400;font-size:10.5px;color:#fff;margin-bottom:10px}
.fcol p{font-size:7.4px;line-height:11.7px;margin-bottom:12px}
.field{width:130px;height:15px;background:#fff;border:1px solid #999;font-size:6px;color:#555;padding:3px 6px;margin-bottom:5px}
.field.tall{height:26px}
.submit{display:inline-block;background:var(--teal);color:#fff;font-size:7px;font-weight:600;padding:3px 13px;margin-top:4px;border-radius:1px}
.wait{color:var(--sky);font-size:9px;margin-bottom:11px}
.bottom{left:0;top:1162px;width:784px;height:38px;background:var(--footer-dark);color:#aaa;font-size:7px;display:flex;justify-content:space-between;align-items:center;padding:0 93px 0 89px}
</style>
</head>
<body>
<div class="abs topbar">
  <span><svg width="6" height="8" viewBox="0 0 6 8"><rect x=".5" y=".5" width="5" height="7" rx="1" fill="none" stroke="#fff"/></svg>+1-555-0142-300</span>
  <span><svg width="9" height="7" viewBox="0 0 9 7"><rect x=".5" y=".5" width="8" height="6" fill="none" stroke="#fff"/><path d="M.5 .5l4 3.5 4-3.5" fill="none" stroke="#fff"/></svg>hello@northvalemed.com</span>
  <span><svg width="8" height="8" viewBox="0 0 8 8"><circle cx="4" cy="4" r="3.5" fill="none" stroke="#fff"/><path d="M4 2v2h2" fill="none" stroke="#fff"/></svg>Monday - Friday</span>
</div>
<div class="abs header"></div>
<div class="abs logo"><i></i>NORTHVALE MEDICAL CENTER</div>
<nav class="abs nav"><span>Why Northvale</span><span>Physician</span><span>Specialities</span><span>Info</span><span>Locations</span><span>Contact Us</span></nav>

<section class="abs hero" role="img" aria-label="Photo of medical staff walking down a bright hospital corridor">
  <h1>Physician Owned Patient Focused</h1>
</section>

<svg class="abs" style="left:0;top:340px" width="784" height="260" viewBox="0 340 784 260">
  <g fill="none" stroke="var(--blue)" stroke-width="1.5">
    <path d="M115.6 415.4A88 88 0 0 1 250.4 415.4M115.6 528.6A88 88 0 0 0 250.4 528.6"/>
    <path d="M331.6 415.4A88 88 0 0 1 466.4 415.4M331.6 528.6A88 88 0 0 0 466.4 528.6"/>
    <path d="M548.6 415.4A88 88 0 0 1 683.4 415.4M548.6 528.6A88 88 0 0 0 683.4 528.6"/>
  </g>
  <g fill="var(--blue)" stroke="#fff" stroke-width="1.5"><circle cx="183" cy="392" r="24"/><circle cx="399" cy="392" r="24"/><circle cx="616" cy="392" r="24"/></g>
  <g fill="none" stroke="#fff" stroke-width="2" stroke-linecap="round">
    <path d="M176 381v8a6 6 0 0 0 12 0v-8M182 395v4a5 5 0 0 0 10 0v-3"/><circle cx="192" cy="394" r="2"/>
    <rect x="389" y="385" width="20" height="15"/><path d="M389 385l10 8 10-8"/>
    <circle cx="616" cy="392" r="10"/>
  </g>
  <text x="616" y="397" text-anchor="middle" fill="#fff" font-family="Arial,sans-serif" font-weight="700" font-size="13">?</text>
  <line x1="251" y1="592" x2="537" y2="592" stroke="#ccc" stroke-dasharray="1 2"/>
  <circle cx="251" cy="592" r="3" fill="#ccc"/><circle cx="537" cy="592" r="3" fill="#ccc"/>
</svg>

<div class="abs feature" style="left:95px;top:428px"><h3>MEDICAL</h3><p>Lorem ipsum dolor sit amet, co ctetuer adipiscing elit, sed di nonummy nibh euismod te.</p><span class="btn">Learn more</span></div>
<div class="abs feature" style="left:311px;top:428px"><h3>EMAIL</h3><p>Lorem ipsum dolor sit amet, co ctetuer adipiscing elit, sed di nonummy nibh euismod te.</p><span class="btn">Learn more</span></div>
<div class="abs feature" style="left:528px;top:428px"><h3>WHY NORTHVALE</h3><p>Lorem ipsum dolor sit amet, co ctetuer adipiscing elit, sed di nonummy nibh euismod te.</p><span class="btn">Learn more</span></div>

<section class="abs cards">
  <article class="card" style="left:8px"><div class="pic" role="img" aria-label="Close-up of a blue eye with glowing globes" style="background:linear-gradient(90deg,#1c3d6e,#6f93c4 50%,#c9d6e8)"></div><h4>Technology</h4><div class="rule"></div><p>Lorem Ipsum is simply dummy text of the printing and typesetting industry. Lorem Ipsum has been the industry's standard dummy text.</p></article>
  <article class="card" style="left:217px"><div class="pic" role="img" aria-label="Quality of care illustration with a stethoscope" style="background:linear-gradient(90deg,#cfe07a,#9fc85a 45%,#3f83b8)"></div><h4>Quality of Care</h4><div class="rule"></div><p>Lorem Ipsum is simply dummy text of the printing and typesetting industry. Lorem Ipsum has been the industry's standard dummy text.</p></article>
  <article class="card" style="left:427px"><div class="pic" role="img" aria-label="Doctor talking with a patient in bed" style="background:linear-gradient(90deg,#eef1f3,#c9d6dc 55%,#8aa3ad)"></div><h4>Patient Experiance</h4><div class="rule"></div><p>Lorem Ipsum is simply dummy text of the printing and typesetting industry. Lorem Ipsum has been the industry's standard dummy text.</p></article>
</section>

<div class="abs welcome-pic" role="img" aria-label="Smiling doctor with a stethoscope"></div>
<section class="abs welcome">
  <h2>Welcome to Northvale Medical</h2>
  <p>This site was created for patients and all people who want information about safe Aesthetic and Reconstructive Plastic Surgery and health in general.</p>
  <p>Undoubtedly, well-informed patients have greater confidence and decision-making ability.</p>
</section>
<section class="abs testi">
  <h2>Testimonials</h2>
  <div class="bubble">Integer vehicula velit quis ante ornare iacu-lis. Sed sed neque metus. Nullam mauris metus, bibendum at facilisis nec, ullamcorper sit amet orci. Nulla facilisi.</div>
  <div class="author"><b>Daniel Whitmore</b><br>CEO, Northvale Medical<span class="avatar"></span></div>
</section>
<div class="abs pager"><i></i><i class="on"></i><i></i><i></i><i></i>&nbsp;NEXT</div>

<footer class="abs footer">
  <div class="fcol" style="left:89px;width:90px"><h5>News</h5><p>Ma quande lingues coalesce, lgrammatica 20/7/2013 plu simplic</p><p>Ma quande lingues coalesce, lgrammatica 20/7/2013 plu simplic</p></div>
  <div class="fcol" style="left:210px;width:120px"><h5>Blog</h5><p>Ma quande lingues coalesce, lgrammatica Ma quande lingues coalesce, lgrammatica plu simplic It va esser tam simplic quam Occidental: in fact, it va esser Occidental. A un Angleso it va semblar un sim-</p></div>
  <div class="fcol" style="left:368px"><h5>Newsletter</h5><div class="field">Enter your name...</div><div class="field">Enter your email</div><div class="field tall">Enter your message</div><span class="submit">SUBMIT</span></div>
  <div class="fcol" style="left:545px;width:155px"><h5>Average Wait Time</h5><div class="wait">9 Minutes</div><p>Lorem ipsum dolor sit amet, consectetuer adipiscing elit, sed diam nonummy nibh euismod tincidunt ut laoreet dolore magna aliquam erat volutpat ed diam nonummy nibh euismod tincidunt ut.</p></div>
</footer>
<div class="abs bottom"><span>Copyright © Northvale Medical. All rights reserved.</span><span>Privacy Policy &nbsp;|&nbsp; Terms &amp; Conditions</span></div>
</body>
</html>
```